Zielgruppe
Alle Männer und Frauen welche fiter in das 2019 starten möchten.
Aufgabenstellung
Es soll ein Flyer sein, der fitnes und dynamic verkörpert.
Es muss darauf ersichtlich sein, dass der 3. Januar 2019 der Start ist für eine 24 Tages challange mit einem Körperreinigungsprogramm.
Ebenfalls muss darauf meine Adresse und Telefonnummer und folgende Punkte:
Körper wird
-gereinigt
-entschlackt
-Hautbild wird verbessert
-Körpergewicht opimiert
-Energielevel steigt
-Essgewohnheiten verbessert

```html
<!DOCTYPE html>
<html lang="de">
<head>
<meta charset="utf-8">
<title>24 Tage Challenge – Flyer</title>
<link href="https://fonts.googleapis.com/css2?family=Cinzel:wght@700;900&family=Nunito:wght@300;400;800&display=swap" rel="stylesheet">
<style>
  :root{
    --purple-dark:#2f1450;
    --purple:#4d2478;
    --purple-light:#6a35a0;
    --green-dark:#2e6a1c;
    --green:#4f9a2c;
    --green-light:#7cc242;
    --white:#ffffff;
    --page:#ffffff;
  }
  *{margin:0;padding:0;box-sizing:border-box}
  html,body{width:1200px;height:848px;overflow:hidden;background:var(--page)}
  body{position:relative;font-family:"Nunito",sans-serif;color:var(--white)}
  .flyer{position:absolute;top:62px;width:328px;height:704px;overflow:hidden}
  .flyer--front{left:229px}
  .flyer--back{left:650px}
  .photo{position:absolute;inset:0}
  .flyer--front .photo{background:radial-gradient(ellipse at 45% 35%,var(--purple-light),var(--purple) 45%,var(--purple-dark) 100%)}
  .flyer--back .photo{background:radial-gradient(ellipse at 45% 45%,var(--green-dark) 0%,var(--green) 55%,var(--green-light) 100%)}
  .strip{position:absolute;top:0;right:0;width:44px;height:100%;display:flex;align-items:center;justify-content:center}
  .flyer--front .strip{background:var(--green)}
  .flyer--back .strip{background:var(--purple-dark)}
  .strip-text{writing-mode:vertical-rl;transform:rotate(180deg);text-align:center;font-size:12.5px;line-height:15px;letter-spacing:.5px;white-space:nowrap}
  .strip-text--contact{font-size:13.5px;letter-spacing:.9px}
  .strip-text b{font-weight:800}
  .badge{position:absolute;left:27px;top:27px;width:106px;height:106px;border-radius:50%;display:flex;flex-direction:column;align-items:center;justify-content:center;font-family:"Cinzel",serif;font-weight:700;font-size:17px;line-height:1.15}
  .flyer--front .badge{background:radial-gradient(circle at 40% 35%,var(--green-light),var(--green) 70%)}
  .flyer--back .badge{background:radial-gradient(circle at 40% 35%,var(--purple-light),var(--purple-dark) 75%)}
  .text{position:absolute;left:27px;white-space:nowrap}
  .lead{font-size:17px;font-weight:300;letter-spacing:.5px;line-height:22px}
  .flyer--back .lead{font-size:20px}
  .headline{font-family:"Cinzel",serif;font-weight:900;font-size:36px;line-height:38px;letter-spacing:.5px}
  .body{font-size:17px;font-weight:300;line-height:23px;letter-spacing:.5px}
  .flyer--back .body{font-size:18px}
  .body b{font-weight:800}
  .arrow{position:absolute}
  .products{position:absolute;left:44px;top:529px;width:288px;height:175px;background:linear-gradient(90deg,#e9e4ef 0%,#cfc4dd 48%,#b8d38f 52%,#7fb43e 100%)}
  .benefits{position:absolute;left:0;top:535px;list-style:none}
  .benefits li{height:17px;margin-bottom:8px;padding-left:29px;padding-right:6px;background:var(--green-light);font-size:13.5px;font-weight:300;line-height:17px;letter-spacing:.6px;width:max-content}
</style>
</head>
<body>

<section class="flyer flyer--front">
  <div class="photo" role="img" aria-label="Läuferin im Lauf, violett eingefärbtes Foto mit Dreiecksmuster"></div>
  <div class="badge"><span>START</span><span>07|01|2019</span></div>
  <p class="text lead" style="top:233px">Starte deine</p>
  <h1 class="text headline" style="top:261px">24 Tage<br>Challenge</h1>
  <p class="text body" style="top:338px">Das<br>Körperreinigungsprogramm</p>
  <svg class="arrow" style="left:166px;top:398px" width="84" height="56" viewBox="0 0 84 56" fill="none" stroke="#fff" stroke-width="2.4" stroke-linecap="round">
    <path d="M4 4 C-2 40 40 54 78 42"/><path d="M68 36 L79 42 L70 50"/>
  </svg>
  <div class="products" role="img" aria-label="Produktverpackungen des 9- und 15-Tage-Programms"></div>
  <aside class="strip">
    <p class="strip-text"><b>Körper</b> reinigen &amp; entschlacken · <b>Hautbild</b> verbessern · <b>Körpergewicht</b> optimieren<br><b>Energielevel</b> steigern · <b>Essgewohnheiten</b> verändern</p>
  </aside>
</section>

<section class="flyer flyer--back">
  <div class="photo" role="img" aria-label="Sportliche Frau im Lauf, grün eingefärbtes Foto mit Dreiecksmuster"></div>
  <div class="badge"><span>START</span><span>03|01|2019</span></div>
  <p class="text lead" style="top:208px">Hole dir jetzt</p>
  <h2 class="text headline" style="top:237px">Weitere<br>Infos</h2>
  <p class="text body" style="top:315px">und starte<br>am <b>07|01|2019</b><br>in dein neues Körpergefühl!</p>
  <svg class="arrow" style="left:175px;top:286px" width="96" height="64" viewBox="0 0 96 64" fill="none" stroke="#fff" stroke-width="2.4" stroke-linecap="round">
    <path d="M6 4 C-2 48 50 64 88 46"/><path d="M78 40 L89 46 L80 55"/>
  </svg>
  <p class="text body" style="top:452px">Mit deinem<br>Körperreinigungsprogramm<br>kannst du in 24 Tagen</p>
  <ul class="benefits">
    <li>deinen Körper entschlacken.</li>
    <li>dein Hautbild verbessern.</li>
    <li>dein Körpergewicht optimieren.</li>
    <li>dein Energielevel steigern.</li>
    <li>deine Essgewohnheiten verändern.</li>
  </ul>
  <aside class="strip">
    <p class="strip-text strip-text--contact"><b>Lukas Brennwald</b> · Lindenweg 12 · 8400 Talheim · Telefon: 078 412 55 60</p>
  </aside>
</section>

</body>
</html>
```